Plainly Query Rowan Consulting needs a new and exciting customer online experience (Webpage)

Plainly Query Rowan is a new and exciting IT and Telecoms business. We aim to help business with all of its technology needs.

The business has only been around less than 12 months and a page was developed to give some online presence, but now its time for a refresh. The page is very bland and boring. It needs some creative zing to give it that pop whilst maintaining a professional appeal.

Our current page can be found at www.plainlyqueryrowan.com.au

I have included below some of our current marketing. I've included our business cards and some of messages on hold we are running.

Target Market(s)

Small to medium business, small enterprise

Industry/Entity Type

Business

Number of Pages Required

5+ page

Font styles to use
Sans Serif

Requirements
Must have
• The page must have some colour. IT and Telecoms can be mundane and boring. We want people to be engaged in their IT and Telecoms. We want them to feel as passionate about their IT and Telecoms as we do.
• It must have the following pages: Home, About Us, Services We provide, Contact Us and our Blog Page.
• The contact us should have an option to complete an online form which is delivered to our enquiries email.
• We would also like to have our social media links for Facebook, LinkedIn and Google plus. The pages must also contain a link to our privacy policy located near the bottom of the page

```html
<!DOCTYPE html>
<html lang="en">
<head>
<meta charset="utf-8">
<title>Blog – Plainly Query Rowan Consulting</title>
<link href="https://fonts.googleapis.com/css2?family=Arimo:wght@400;700&family=Source+Sans+3:wght@400;600;700&display=swap" rel="stylesheet">
<style>
:root{
  --navy:#3a3f66;
  --blue:#1aa3d9;
  --green:#7ab51d;
  --red:#d9183b;
  --link:#e0443d;
  --teal:#48b0a4;
  --text:#444;
  --muted:#777;
  --rule:#e2e2e2;
  --footer:#14719a;
  --footer-dark:#0d5d80;
}
*{box-sizing:border-box;margin:0;padding:0}
html,body{width:979px;height:1200px;overflow:hidden;background:#fff}
body{position:relative;font-family:"Arimo",Arial,sans-serif;color:var(--text);font-size:11px}
a{text-decoration:none;color:inherit}
.abs{position:absolute}

.stripe{position:absolute;top:0;left:0;width:979px;height:3px;
  background:linear-gradient(90deg,#e04a3b 0 10%,#f08a3c 10% 20%,#9fd7c8 20% 32%,#5aa98f 32% 42%,#f4b400 42% 52%,#8fd3c1 52% 62%,#e04a3b 62% 72%,#f08a3c 72% 80%,#f4b400 80% 90%,#5aa98f 90% 100%)}
.header{position:absolute;top:3px;left:0;width:979px;height:63px;background:#fff}
.brand{position:absolute;left:106px;top:9px;display:flex;align-items:center;gap:10px}
.brand-mark{width:34px;height:34px;border-radius:50%;background:var(--blue)}
.brand-name{font-family:"Source Sans 3",sans-serif;font-weight:600;font-size:20px;line-height:20px;color:var(--navy)}
.main-nav{position:absolute;right:109px;top:27px;display:flex;gap:17px;font-size:11px;color:#555}
.main-nav .sep{color:#777}
.main-nav .active{color:var(--blue)}

.subbar{position:absolute;top:66px;left:0;width:979px;height:58px;background:linear-gradient(#fff,#ececec);border-bottom:3px solid var(--navy)}
.promo{position:absolute;top:15px;font-size:11px;line-height:14px;letter-spacing:.3px}
.promo b{display:block;font-weight:700;color:var(--green)}
.promo.call b{color:var(--red)}
.promo-div{position:absolute;top:12px;height:36px;border-left:1px dashed #ccc}
.search{position:absolute;left:673px;top:17px;width:211px;height:21px;border:1px solid #ddd;background:#fff;border-radius:2px;font-size:10px;color:#999;padding:4px 8px}
.search-btn{position:absolute;right:2px;top:2px;width:30px;height:15px;background:var(--green);border-radius:2px}

.crumb{position:absolute;top:136px;left:106px;font-size:10px;color:#666}
.crumb a{color:var(--red)}
.page-title{position:absolute;top:174px;left:106px;font-family:"Source Sans 3",sans-serif;font-weight:400;font-size:19px;color:#333}
.banner{position:absolute;top:201px;left:106px;width:779px;height:107px;background:linear-gradient(90deg,#79a62b 0%,#8cb83a 55%,#c9d6b8 75%,#e8e4e0 100%);border-bottom:2px solid #ddd}
.banner span{position:absolute;left:29px;top:42px;font-family:"Source Sans 3",sans-serif;font-weight:600;font-size:21px;color:#fff}

.post{position:absolute;left:108px;width:538px;height:200px;border-bottom:3px solid var(--rule)}
.date{position:absolute;left:0;top:0;width:56px;height:64px;background:var(--blue);color:#fff;text-align:center;box-shadow:0 2px 2px #ccc;font-family:"Source Sans 3",sans-serif}
.date .m{font-size:17px;padding-top:7px;line-height:18px}
.date .d{font-size:25px;font-weight:700;line-height:28px}
.type{position:absolute;left:0;top:82px;width:56px;height:56px;background:var(--red);box-shadow:0 2px 2px #ccc;display:flex;align-items:center;justify-content:center}
.post-title{position:absolute;left:80px;top:0;font-family:"Source Sans 3",sans-serif;font-weight:600;font-size:16px;color:#333;white-space:nowrap}
.meta{position:absolute;left:80px;top:31px;font-family:"Source Sans 3",sans-serif;font-size:11px;color:var(--muted);display:flex;align-items:center}
.meta a{color:var(--link)}
.meta .tags{margin-left:32px;display:flex;align-items:center;gap:5px}
.meta .count{margin-left:14px;display:flex;align-items:center;gap:5px;color:var(--link)}
.excerpt{position:absolute;left:80px;top:65px;width:460px;font-size:10.3px;line-height:17px;color:#555}
.more{position:absolute;left:80px;top:152px;font-family:"Source Sans 3",sans-serif;font-size:11px;color:var(--link);display:flex;align-items:center;gap:8px}

.pager{position:absolute;left:107px;top:1043px;display:flex;gap:5px}
.pager span{width:16px;height:16px;background:#8f9596;color:#fff;font-size:6px;font-weight:700;display:flex;align-items:center;justify-content:center;border-radius:1px}
.pager .current{background:var(--green)}
.pager .hover{background:var(--red)}
.pager .gap{margin-left:8px}

.side-title{position:absolute;left:699px;font-family:"Source Sans 3",sans-serif;font-weight:400;font-size:13px;color:#707b80}
.cats{position:absolute;left:709px;top:381px;list-style:none}
.cats li{height:24.5px;display:flex;align-items:center;gap:10px;font-family:"Source Sans 3",sans-serif;font-size:11.5px;color:var(--red)}
.recent{position:absolute;left:699px;top:567px;width:221px;list-style:none}
.recent li{border-bottom:1px solid var(--rule);padding:2px 0 6px 25px;position:relative;margin-bottom:8px}
.recent li::before{content:"›";position:absolute;left:10px;top:0;color:var(--teal);font-size:14px;line-height:14px}
.recent a{display:block;font-family:"Source Sans 3",sans-serif;font-weight:700;font-size:11.5px;line-height:17px;color:var(--red)}
.recent small{font-family:"Source Sans 3",sans-serif;font-size:9px;color:#666}

.footer{position:absolute;top:1102px;left:0;width:979px;height:98px;background:linear-gradient(90deg,var(--footer-dark) 0%,var(--footer) 50%,#2eb3dc 100%)}
.foot-nav{position:absolute;left:107px;top:22px;display:flex;gap:24px;font-size:9.5px;color:#fff;letter-spacing:.4px}
.social{position:absolute;left:448px;top:18px;display:flex;gap:4px}
.social span{width:18px;height:18px;border-radius:50%;background:#fff;opacity:.85}
.legal{position:absolute;left:107px;top:50px;font-size:9.5px;color:#fff;letter-spacing:.3px}
.subscribe{position:absolute;left:676px;top:1085px;width:198px;height:115px;background:#08597a;color:#fff}
.subscribe::before{content:"";position:absolute;left:12px;top:-7px;width:174px;height:7px;background:#8a8a8a;border-radius:3px 3px 0 0}
.subscribe h3{position:absolute;left:79px;top:22px;font-size:12px;line-height:15px;font-weight:700;letter-spacing:.5px}
.sub-form{position:absolute;left:20px;top:60px;width:162px;height:20px;border:1px solid #fff;display:flex}
.sub-form span{flex:1;font-size:9.5px;padding:4px 5px}
.sub-form b{width:28px;background:#fff;color:#333;font-size:9px;display:flex;align-items:center;justify-content:center;font-weight:400}
.sub-note{position:absolute;left:22px;top:88px;font-size:9.5px}
</style>
</head>
<body>
<div class="stripe"></div>

<header class="header">
  <a class="brand" href="#"><span class="brand-mark"></span><span class="brand-name">Plainly Query Rowan<br>Consulting</span></a>
  <nav class="main-nav">
    <a class="active" href="#">Home</a><span class="sep">/</span>
    <a href="#">About Us</a><span class="sep">/</span>
    <a href="#">Services We provide</a><span class="sep">/</span>
    <a href="#">Contact Us</a><span class="sep">/</span>
    <a href="#">Our Blog</a>
  </nav>
</header>

<section class="subbar">
  <div class="promo" style="left:108px"><b>What</b>Can we help with</div>
  <div class="promo-div" style="left:211px"></div>
  <div class="promo" style="left:235px"><b>How</b>Can we help</div>
  <div class="promo-div" style="left:368px"></div>
  <div class="promo" style="left:391px"><b>Why</b>Not contact us</div>
  <div class="promo-div" style="left:497px"></div>
  <div class="promo call" style="left:533px"><b>Call Us Today!</b>(08) 5550 1234</div>
  <div class="promo-div" style="left:644px"></div>
  <div class="search">Looking for somthing
    <span class="search-btn"><svg width="30" height="15" viewBox="0 0 30 15"><circle cx="14" cy="6.5" r="3.5" fill="none" stroke="#fff" stroke-width="1.6"/><line x1="16.5" y1="9" x2="19" y2="11.5" stroke="#fff" stroke-width="1.8"/></svg></span>
  </div>
</section>

<div class="crumb"><a href="#">Home</a> &nbsp;›&nbsp; Blog</div>
<h1 class="page-title">Blog</h1>
<div class="banner" role="img" aria-label="Photo of a finger pressing a green blog key on a keyboard"><span>Plainly Query Rowan Consulting</span></div>

<article class="post" style="top:342px">
  <div class="date"><div class="m">MAY</div><div class="d">26</div></div>
  <div class="type"><svg width="18" height="22" viewBox="0 0 18 22"><path d="M2 1h9l5 5v15H2z" fill="none" stroke="#fff" stroke-width="2"/><path d="M5 11h8M5 14h8M5 17h8" stroke="#fff" stroke-width="1.6"/></svg></div>
  <h2 class="post-title">Duis dapibus aliquam mi, eget euismod sem scelerisque ut.</h2>
  <div class="meta">Posted by&nbsp;<a href="#">Admin</a>&nbsp;in&nbsp;<a href="#">Blogsmith</a>
    <span class="tags"><svg width="14" height="10" viewBox="0 0 14 10"><path d="M0 0h7l5 5-5 5H0z" fill="var(--teal)"/></svg><a href="#">Design, Template</a></span>
    <span class="count"><svg width="14" height="10" viewBox="0 0 14 10"><ellipse cx="7" cy="4.5" rx="6" ry="4" fill="var(--teal)"/></svg>22</span></div>
  <p class="excerpt">Maecenas eget turpis turpis. Nunc vel metus augue. Aenean euismod cursus ligula eget dapibus. Praesent vel erat in tortor placerat dignissim. Duis dapibus aliquam mi, eget euismod sem scelerisque ut. Vivamus at elit quis urna adipiscing iaculis. Curabitur vitae velit in neque dictum blandit. Proin in iaculis neque. Pellentesque habitant morbi tristique senectus et netus</p>
  <a class="more" href="#">Continue reading <svg width="11" height="10" viewBox="0 0 11 10"><path d="M0 5h8M5 1l4 4-4 4" stroke="var(--link)" stroke-width="2" fill="none"/></svg></a>
</article>

<article class="post" style="top:579px">
  <div class="date"><div class="m">MAY</div><div class="d">26</div></div>
  <div class="type"><svg width="18" height="22" viewBox="0 0 18 22"><path d="M2 1h9l5 5v15H2z" fill="none" stroke="#fff" stroke-width="2"/><path d="M5 11h8M5 14h8M5 17h8" stroke="#fff" stroke-width="1.6"/></svg></div>
  <h2 class="post-title">Duis dapibus aliquam mi, eget euismod sem scelerisque ut.</h2>
  <div class="meta">Posted by&nbsp;<a href="#">Admin</a>&nbsp;in&nbsp;<a href="#">Blogsmith</a>
    <span class="tags"><svg width="14" height="10" viewBox="0 0 14 10"><path d="M0 0h7l5 5-5 5H0z" fill="var(--teal)"/></svg><a href="#">Design, Template</a></span>
    <span class="count"><svg width="14" height="10" viewBox="0 0 14 10"><ellipse cx="7" cy="4.5" rx="6" ry="4" fill="var(--teal)"/></svg>22</span></div>
  <p class="excerpt">Maecenas eget turpis turpis. Nunc vel metus augue. Aenean euismod cursus ligula eget dapibus. Praesent vel erat in tortor placerat dignissim. Duis dapibus aliquam mi, eget euismod sem scelerisque ut. Vivamus at elit quis urna adipiscing iaculis. Curabitur vitae velit in neque dictum blandit. Proin in iaculis neque. Pellentesque habitant morbi tristique senectus et netus</p>
  <a class="more" href="#">Continue reading <svg width="11" height="10" viewBox="0 0 11 10"><path d="M0 5h8M5 1l4 4-4 4" stroke="var(--link)" stroke-width="2" fill="none"/></svg></a>
</article>

<article class="post" style="top:809px">
  <div class="date"><div class="m">MAY</div><div class="d">26</div></div>
  <div class="type"><svg width="18" height="22" viewBox="0 0 18 22"><path d="M2 1h9l5 5v15H2z" fill="none" stroke="#fff" stroke-width="2"/><path d="M5 11h8M5 14h8M5 17h8" stroke="#fff" stroke-width="1.6"/></svg></div>
  <h2 class="post-title">Duis dapibus aliquam mi, eget euismod sem scelerisque ut.</h2>
  <div class="meta">Posted by&nbsp;<a href="#">Admin</a>&nbsp;in&nbsp;<a href="#">Blogsmith</a>
    <span class="tags"><svg width="14" height="10" viewBox="0 0 14 10"><path d="M0 0h7l5 5-5 5H0z" fill="var(--teal)"/></svg><a href="#">Design, Template</a></span>
    <span class="count"><svg width="14" height="10" viewBox="0 0 14 10"><ellipse cx="7" cy="4.5" rx="6" ry="4" fill="var(--teal)"/></svg>22</span></div>
  <p class="excerpt">Maecenas eget turpis turpis. Nunc vel metus augue. Aenean euismod cursus ligula eget dapibus. Praesent vel erat in tortor placerat dignissim. Duis dapibus aliquam mi, eget euismod sem scelerisque ut. Vivamus at elit quis urna adipiscing iaculis. Curabitur vitae velit in neque dictum blandit. Proin in iaculis neque. Pellentesque habitant morbi tristique senectus et netus</p>
  <a class="more" href="#">Continue reading <svg width="11" height="10" viewBox="0 0 11 10"><path d="M0 5h8M5 1l4 4-4 4" stroke="var(--link)" stroke-width="2" fill="none"/></svg></a>
</article>

<nav class="pager">
  <span>‹</span><span class="gap">1</span><span class="current">2</span><span>3</span><span>4</span><span>5</span><span>…</span><span>10</span><span class="hover">11</span><span>12</span><span class="gap">›</span>
</nav>

<h2 class="side-title" style="top:343px">CATEGORIES</h2>
<ul class="cats">
  <li><svg width="11" height="11" viewBox="0 0 11 11"><circle cx="5.5" cy="5.5" r="5.5" fill="var(--teal)"/><path d="M3 5.5h4.5M5.5 3.3l2.2 2.2-2.2 2.2" stroke="#fff" stroke-width="1.3" fill="none"/></svg>LOGO DESIGN</li>
  <li><svg width="11" height="11" viewBox="0 0 11 11"><circle cx="5.5" cy="5.5" r="5.5" fill="var(--teal)"/><path d="M3 5.5h4.5M5.5 3.3l2.2 2.2-2.2 2.2" stroke="#fff" stroke-width="1.3" fill="none"/></svg>WEB DESIGN</li>
  <li><svg width="11" height="11" viewBox="0 0 11 11"><circle cx="5.5" cy="5.5" r="5.5" fill="var(--teal)"/><path d="M3 5.5h4.5M5.5 3.3l2.2 2.2-2.2 2.2" stroke="#fff" stroke-width="1.3" fill="none"/></svg>PHOTOGRAPHY</li>
  <li><svg width="11" height="11" viewBox="0 0 11 11"><circle cx="5.5" cy="5.5" r="5.5" fill="var(--teal)"/><path d="M3 5.5h4.5M5.5 3.3l2.2 2.2-2.2 2.2" stroke="#fff" stroke-width="1.3" fill="none"/></svg>BLOGSMITH</li>
  <li><svg width="11" height="11" viewBox="0 0 11 11"><circle cx="5.5" cy="5.5" r="5.5" fill="var(--teal)"/><path d="M3 5.5h4.5M5.5 3.3l2.2 2.2-2.2 2.2" stroke="#fff" stroke-width="1.3" fill="none"/></svg>ICONS</li>
</ul>

<h2 class="side-title" style="top:530px">RECENT POSTS</h2>
<ul class="recent">
  <li><a href="#">Curabitur vitae velit</a><small>25 May 2013</small></li>
  <li><a href="#">Vivamus at elit quis urna adipiscing iaculis</a><small>25 May 2013</small></li>
  <li><a href="#">Curabitur vitae velit</a><small>25 May 2013</small></li>
  <li><a href="#">Vivamus at elit quis urna adipiscing iaculis</a><small>25 May 2013</small></li>
</ul>

<footer class="footer">
  <nav class="foot-nav"><a href="#">HOME</a><a href="#">ABOUT US</a><a href="#">WHAT WE DO</a><a href="#">BLOG</a><a href="#">CONTACT</a></nav>
  <div class="social"><span></span><span></span><span></span></div>
  <p class="legal">Copyright 2014 | Disclaimer | Privacy Policy</p>
</footer>

<aside class="subscribe">
  <svg class="abs" style="left:22px;top:20px" width="30" height="28" viewBox="0 0 30 28"><path d="M2 10l13-8 13 8v16H2z" fill="none" stroke="#fff" stroke-width="1.5"/><path d="M6 4h18v14H6z" fill="#08597a" stroke="#fff" stroke-width="1.2"/><path d="M9 8h12M9 11h12M9 14h12" stroke="#fff"/><path d="M2 26l13-9 13 9" fill="none" stroke="#fff" stroke-width="1.5"/></svg>
  <h3>Subscribe<br>for News Letters</h3>
  <div class="sub-form"><span>Enter Your Email Address</span><b>GO</b></div>
  <p class="sub-note">Sign up now for more information</p>
</aside>
</body>
</html>
```